Informational Landing Page Redesign

Pure Stream Filter Guide, reviews and provides information about water ionizers for users. The web site is supposed to be an "expert or researched based" We are looking to redesign the following landing page:

http://www.purestreamfilterguide.example/learn/what-is-alkaline-water

The design should be geared towards converting visitors into leads. We are looking for a redesign of the content section. The header and footer should be the same as the current site. The text and colors should be consistent with the current site but please feel free to make bold choices that work and add stock photos.

Target Market(s)

Ages 45+ with disposable income.

Industry/Entity Type

Learn

Requirements
Must have
• The page must have the all current content. It also should have a web site form placed above the fold.

Please note you can change the designs of the "advertisements".
Nice to have
• Placement of social media elements so users can spread the page to friends, example facebook and google+ like buttons. A banner area that is capable of holding a rotating banner or video or banner.
Should not have
• Distractions from the goal, converting users to leads.
Distractions from the content, since the user is there to read.
Missing information and text, all information on the current page should appear on the redesign.

Deviations from the current header and footer.

```html
<!DOCTYPE html>
<html lang="en">
<head>
<meta charset="utf-8">
<title>What is Alkaline Water? – Pure Stream Filter Guide</title>
<link href="https://fonts.googleapis.com/css2?family=PT+Sans+Narrow:wght@400;700&family=Ubuntu:wght@300;400;500&family=Open+Sans:wght@400;600;700&display=swap" rel="stylesheet">
<style>
  :root{
    --blue:#1f7fc2;
    --blue-dark:#1467a6;
    --blue-band:#3f9fe0;
    --nav-blue:#2a86c8;
    --orange:#f08a1a;
    --orange-dark:#e07405;
    --text:#555;
    --text-dark:#333;
    --line:#dcdcdc;
    --page-bg:#efefef;
    --panel:#ffffff;
  }
  *{box-sizing:border-box;margin:0;padding:0}
  html,body{width:901px;height:1200px;overflow:hidden}
  body{background:var(--page-bg);font-family:"Ubuntu",sans-serif;color:var(--text);position:relative}
  .abs{position:absolute}

  /* header */
  .site-header{position:absolute;left:0;top:0;width:901px;height:109px;background:linear-gradient(#fff,#f6f6f6);border-bottom:1px solid #e2e2e2}
  .brand{position:absolute;left:62px;top:28px;display:flex;align-items:center;gap:10px}
  .brand-mark{width:40px;height:40px;border-radius:50%;background:var(--blue)}
  .brand-name{font-family:"Open Sans",sans-serif;font-weight:600;font-size:18px;line-height:22px;color:#555;width:190px}
  .brand-tag{position:absolute;left:115px;top:75px;font-family:"Open Sans",sans-serif;font-size:10.5px;color:#666;background:#eee;padding:0 3px}
  .social{position:absolute;left:735px;top:8px;display:flex;gap:4px}
  .social span{width:16px;height:16px;border-radius:2px;background:#8a8a8a}
  .social span:nth-child(2){background:#3aa34a}
  .social span:nth-child(3){background:#3aa3dc}
  .social span:nth-child(4){background:#3c64a8}
  .main-nav{position:absolute;left:379px;top:36px;width:449px;height:30px;border-top:1px solid #e0e0e0;border-bottom:1px solid #e0e0e0;background:#f3f3f3;display:flex;justify-content:space-around;align-items:center}
  .main-nav a{font-family:"Open Sans",sans-serif;font-weight:700;font-size:14px;color:var(--nav-blue);text-decoration:none}
  .btn-guide{position:absolute;left:738px;top:73px;width:91px;height:27px;border-radius:3px;background:linear-gradient(#f79a2a,var(--orange-dark));color:#fff;font-family:"Open Sans",sans-serif;font-weight:700;font-size:11px;display:flex;align-items:center;justify-content:center}

  /* banner */
  .banner{position:absolute;left:0;top:109px;width:901px;height:282px;background:linear-gradient(#6bb8ec,var(--blue-band) 60%,#2c8ad2)}
  .slider{position:absolute;left:57px;top:10px;width:786px;height:262px;background:#fff;padding:4px;border-radius:2px}
  .slide-img{width:778px;height:254px;background:linear-gradient(100deg,#9fd4ef 0%,#dff2fb 45%,#e9f6fb 70%,#b9e0f3 100%)}
  .slider-arrow{position:absolute;top:121px;width:24px;height:40px;background:var(--blue);display:flex;align-items:center;justify-content:center}
  .slider-arrow.prev{left:0;border-radius:0 20px 20px 0}
  .slider-arrow.next{right:-4px;border-radius:20px 0 0 20px}
  .dots{position:absolute;left:370px;top:251px;display:flex;gap:3px;background:rgba(255,255,255,.6);padding:3px 4px;border-radius:6px}
  .dots i{width:7px;height:7px;border-radius:50%;background:#888}
  .dots i:first-child{background:var(--blue)}

  /* content panel */
  .panel{position:absolute;left:56px;top:391px;width:788px;height:809px;background:var(--panel)}
  .article{position:absolute;left:17px;top:20px;width:483px}
  .article h1{font-family:"PT Sans Narrow",sans-serif;font-weight:700;font-size:20px;color:var(--blue);margin-bottom:4px}
  .article p{font-size:9.2px;line-height:15.5px;margin-bottom:3.5px;color:var(--text)}
  .minerals{list-style:none;margin:8px 0 10px 4px}
  .minerals li{font-size:9.5px;color:var(--text-dark);line-height:19.5px;padding-left:9px;position:relative}
  .minerals li::before{content:"";position:absolute;left:0;top:7px;border-left:4px solid #444;border-top:3px solid transparent;border-bottom:3px solid transparent}
  .divider{position:absolute;left:19px;top:369px;width:480px;height:1px;background:var(--line)}

  .box{position:absolute;top:395px;width:237px;height:285px;border:1px solid #e4e4e4;background:#fff}
  .box-head{height:36px;font-family:"PT Sans Narrow",sans-serif;font-weight:700;font-size:18px;color:#fff;padding:8px 17px}
  .box.download{left:17px}
  .box.download .box-head{background:linear-gradient(#f7a034,var(--orange-dark))}
  .box.resources{left:264px}
  .box.resources .box-head{background:linear-gradient(#5ab1ea,var(--blue-dark))}
  .box-body{padding:18px 15px 0}
  .lead-title{font-size:9.5px;font-weight:500;color:var(--text-dark)}
  .lead-sub{font-size:9px;color:var(--text);margin-top:4px}
  .field-label{font-size:9.5px;color:var(--text-dark);margin-top:14px}
  .field{width:185px;height:23px;border:1px solid #cfcfcf;border-radius:3px;margin-top:2px;font-size:8.5px;font-style:italic;color:#888;padding:6px 8px}
  .btn-download{position:absolute;left:111px;top:235px;width:88px;height:23px;border-radius:3px;background:linear-gradient(#f79a2a,var(--orange-dark));color:#fff;font-family:"PT Sans Narrow",sans-serif;font-weight:700;font-size:12px;text-align:center;line-height:23px}
  .res-intro{font-size:9px;line-height:15.5px;color:var(--text)}
  .res-intro strong{font-weight:500;color:var(--text-dark)}
  .res-list{list-style:none;margin-top:14px}
  .res-list li{height:25.5px;display:flex;align-items:center;gap:8px;font-size:9px;color:var(--text-dark);border-bottom:1px solid #ececec;width:190px}
  .res-list li:last-child{border-bottom:none}
  .res-list li i{width:13px;height:13px;border-radius:50%;background:#e3e3e3;position:relative;flex:none}
  .res-list li i::after{content:"";position:absolute;left:5px;top:4px;border-left:3px solid #555;border-top:2.5px solid transparent;border-bottom:2.5px solid transparent}

  .sidebar-title{position:absolute;left:533px;top:24px;font-family:"PT Sans Narrow",sans-serif;font-weight:700;font-size:19px;color:var(--text-dark)}
  .video{position:absolute;left:533px;top:52px;width:240px;height:182px;background:linear-gradient(135deg,#9fc9e6,#e6f1f6 50%,#7fa9c4)}
  .play{position:absolute;left:100px;top:70px;width:42px;height:42px;border-radius:50%;border:3px solid #fff;background:rgba(0,0,0,.25)}
  .play::after{content:"";position:absolute;left:14px;top:10px;border-left:14px solid #fff;border-top:8px solid transparent;border-bottom:8px solid transparent}
  .ad-deals{position:absolute;left:540px;top:253px;width:227px;height:192px;background:linear-gradient(#2d8ad0,#1f6fb4);color:#fff;text-align:center;font-family:"Open Sans",sans-serif;overflow:hidden}
  .ad-deals .l1{font-size:17px;line-height:22px;margin-top:4px}
  .ad-deals .l3{font-family:"Open Sans",sans-serif;font-weight:700;font-size:22px;letter-spacing:2px;margin-top:6px}
  .ad-products{width:160px;height:68px;margin:6px auto 0;background:linear-gradient(90deg,#1d1d1d 0 40%,transparent 40% 60%,#c8ccd0 60%)}
  .ad-deals .l4{font-size:14px;margin-top:8px}
  .ad-lifestyle{position:absolute;left:540px;top:457px;width:227px;height:199px;background:linear-gradient(160deg,#e8f3dc,#cfe6b0 55%,#7fbf3f)}

  .footer-line{position:absolute;left:19px;top:709px;width:752px;height:1px;background:var(--line)}
  .footer-brand{position:absolute;left:24px;top:728px;display:flex;align-items:center;gap:8px}
  .footer-brand .brand-mark{width:30px;height:30px}
  .footer-brand .brand-name{font-size:13.5px;line-height:16px;width:140px}
  .footer-tag{position:absolute;left:62px;top:761px;font-family:"Open Sans",sans-serif;font-size:8px;color:#666;background:#eee;padding:0 3px}
  .copyright{position:absolute;right:38px;top:727px;font-size:9px;color:var(--text)}
  .footer-nav{position:absolute;right:38px;top:748px;font-size:10px;color:var(--nav-blue)}
  .footer-nav span{color:var(--nav-blue);margin:0 6px}
</style>
</head>
<body>
  <header class="site-header">
    <div class="brand"><span class="brand-mark"></span><span class="brand-name">PURE STREAM FILTER GUIDE</span></div>
    <div class="brand-tag">Find the perfect Water Ionizer.</div>
    <div class="social" aria-label="Share"><span></span><span></span><span></span><span></span></div>
    <nav class="main-nav"><a>HOME</a><a>REVIEWS</a><a>LEARN</a><a>COMPARE</a><a>BLOG</a><a>ABOUT US</a></nav>
    <div class="btn-guide">Buyer's Guide</div>
  </header>

  <section class="banner">
    <div class="slider">
      <div class="slide-img" role="img" aria-label="Splashing water beside white tulips and a yellow butterfly against a blue sky"></div>
      <div class="slider-arrow prev"><svg width="8" height="12"><path d="M6 1 1 6l5 5" stroke="#fff" stroke-width="2.5" fill="none"/></svg></div>
      <div class="slider-arrow next"><svg width="8" height="12"><path d="M2 1l5 5-5 5" stroke="#fff" stroke-width="2.5" fill="none"/></svg></div>
      <div class="dots"><i></i><i></i><i></i><i></i></div>
    </div>
  </section>

  <main class="panel">
    <article class="article">
      <h1>What is Alkaline Water?</h1>
      <p>The Water Ionizer industry is chalked full of confusing information. They often throw around machine specifications and technical jargon that needs to be dissected and explained in order to be understood. Our team at Pure Stream Filter Guide is hoping to avoid this by giving you only the facts you need.</p>
      <p>We have written this information coherently so you may understand the properties of alkaline water and how it benefits you. We want your next Water Ionizer purchase to be clear and informed. So let's start with the basics, what exactly is alkaline water?</p>
      <p>Simply put, alkaline water is water with a potential hydrogen (pH) value of more than 7 (7 being neutral on the pH scale). Typically in the water ionizer industry, this is achieved using a process known as "electrodialysis". This process splits the neutral water into 2 types, acidic and alkaline. Both have their unique benefits and properties, but alkaline water is filled with healthy minerals like:</p>
      <ul class="minerals"><li>Calcium</li><li>Magnesium</li><li>Potassium</li></ul>
      <p>While unhealthy minerals like fluoride, nitrates, and sulfides, are flushed out through the acidic water.</p>
      <p>Besides the ability to eliminate the harmful toxins that are found in most tap water, there are numerous health benefits to alkaline water – all of which are backed by research. Leaders in the health and fitness industry have attested to the advantages of alkaline water for years. Maybe it's time you discovered the real power of Alkaline Water for yourself?</p>
    </article>
    <div class="divider"></div>

    <section class="box download">
      <div class="box-head">Download Start Here</div>
      <div class="box-body">
        <div class="lead-title">Download your free Buyer's Guide now!</div>
        <div class="lead-sub">Vivamus porttitor, neque at volutpat.</div>
        <div class="field-label">Your Name:</div><div class="field">name goes here</div>
        <div class="field-label">Phone no:</div><div class="field">phone no. goes here</div>
        <div class="field-label">E-mail address:</div><div class="field">email add goes here</div>
      </div>
      <div class="btn-download">Download</div>
    </section>

    <section class="box resources">
      <div class="box-head">Resources</div>
      <div class="box-body">
        <p class="res-intro"><strong>Suspendisse quam leo, molestie sed</strong> luctus quis, feugiat in, pede. Fusce tellus. Sed metus augue, convallis et, vehicula ut.</p>
        <ul class="res-list">
          <li><i></i>What is Alkaline Water?</li>
          <li><i></i>Benefits of Alkaline Water</li>
          <li><i></i>What is Acidic Water?</li>
          <li><i></i>Benefits of Acidic Water</li>
          <li><i></i>What are pH and ORP?</li>
          <li><i></i>How do Ionizers work?</li>
        </ul>
      </div>
    </section>

    <h2 class="sidebar-title">How it Works</h2>
    <div class="video" role="img" aria-label="Video still of a microscope and glass flasks with green plants"><span class="play"></span></div>
    <div class="ad-deals">
      <div class="l1">Find the <b>best deals</b><br>on Water Ionizers</div>
      <div class="l3">GUARANTEED</div>
      <div class="ad-products" role="img" aria-label="Two countertop water ionizer units"></div>
      <div class="l4">Talk to an expert today!</div>
    </div>
    <div class="ad-lifestyle" role="img" aria-label="Alkaline lifestyle banner with green leaves and the words nutrition, fitness, mind and spirit"></div>

    <div class="footer-line"></div>
    <div class="footer-brand"><span class="brand-mark"></span><span class="brand-name">PURE STREAM FILTER GUIDE</span></div>
    <div class="footer-tag">Find the perfect Water Ionizer.</div>
    <div class="copyright">© 2009-2012 Pure Stream Filter Guide. All Rights Reserved | Read our Privacy Policy.</div>
    <nav class="footer-nav">Home<span>|</span>Reviews<span>|</span>Learn<span>|</span>Compare<span>|</span>Blog<span>|</span>About Us<span>|</span>Buyer's Guide</nav>
  </main>
</body>
</html>
```